Luxury Jewelry & Watch Company Website Design

At Vexaro, we are a brand that designs and sells unique Jewelry & Watches for Men and Women. We are looking to transform our current e-commerce website, which looks like a boring catalog, into a more EXCLUSIVE, luxurious, and unique website experience... CLASSY, yet MODERN...We want customers/ clients to be drawn into our brand and our products.. essentially to turn them into buying customers. We want them to feel the exclusiveness of our brand and how different we are from the rest of the industry. The website has to convey the feel and culture of our brand, but stay simple to navigate.

We sell direct to the consumer online as well as wholesale to retailers, And now we are opening our first store in March..So the website should appeal to all areas. Id like to have a place on the website for our upcoming store, it would be sweet to have an area where clients can setup an appointment to meet with me at the store to go over and Jewelry, watches, or Custom Jewelry Design. In March, we will have professional photos of the store as well as professional photos of models wearing the Jewelry & Watches. So please make space for all of those new photos to be implemented.

That should be it! It all comes down to creating a Luxurious, Exclusive, and Unique website that portrays Vexaro and brings in clientele and seals the deal for sales!

Thank you very much! We are extremely excited to see all your awesome designs!

Target Market(s)

25-40 year old successful Men & Women... The young professionals crowd.

Industry/Entity Type

E-Commerce

Requirements
Must have
• Luxury, Exclusive feeling (like Corvane, Marrow Peak Vodka, ext), Simplicity, Brand Culture, Watches are our main product, Appeal to both Men & Women. Also, an elegant banner for promotions, that i am able to update myself.
Nice to have
• Store Appointment Scheduler, updated area that shows which celebs/ stars are wearing the goods, History of the brand and products

```html
<!DOCTYPE html>
<html lang="en">
<head>
<meta charset="utf-8">
<title>Vexaro — Jewelry &amp; Watches</title>
<link href="https://fonts.googleapis.com/css2?family=Arvo&family=PT+Sans:wght@400;700&display=swap" rel="stylesheet">
<style>
  :root{
    --page:#f0f0f0;
    --topbar:#262626;
    --header-top:#f3f3f3;
    --header-bottom:#e4e4e4;
    --ink:#2e2e2e;
    --text:#444;
    --accent:#6b3a41;
    --accent-dark:#4e2a30;
    --rule:#c9c9c9;
    --footer:#272727;
    --footer-base:#1b1b1b;
    --footer-text:#c4c4c4;
    --icon:#333;
  }
  *{box-sizing:border-box;margin:0;padding:0}
  html,body{width:1025px;height:1200px;overflow:hidden}
  body{background:var(--page);font-family:"PT Sans",sans-serif;color:var(--text);position:relative}

  .topbar{position:absolute;left:0;top:0;width:1025px;height:28px;background:var(--topbar)}
  .appointment{position:absolute;left:630px;top:7px;font:700 11px "PT Sans",sans-serif;color:#eee;letter-spacing:.2px}
  .appointment-sep{position:absolute;left:741px;top:6px;color:#777;font-size:12px}
  .search{position:absolute;left:757px;top:5px;width:117px;height:19px;background:#f4f4f4;border-radius:3px;font-size:10px;color:#555;padding:3px 6px}
  .search svg{position:absolute;right:5px;top:3px}

  .site-header{position:absolute;left:0;top:28px;width:1025px;height:72px;background:linear-gradient(var(--header-top),var(--header-bottom));border-bottom:1px solid #bdbdbd;box-shadow:0 2px 3px rgba(0,0,0,.15)}
  .brand{position:absolute;left:178px;top:14px;font:400 38px "PT Sans",sans-serif;color:#141414;letter-spacing:1px}
  .main-nav{position:absolute;left:464px;top:0;height:72px;display:flex}
  .main-nav a{display:block;height:72px;line-height:72px;padding:0 13px;font:700 12px "PT Sans",sans-serif;color:#333;text-decoration:none;border-left:1px solid #d2d2d2}
  .main-nav a:first-child{border-left:none}
  .main-nav a.current{color:var(--accent)}

  .hero{position:absolute;left:137px;top:100px;width:743px;height:462px;background:#fff;box-shadow:0 1px 3px rgba(0,0,0,.1)}
  .hero-photo{position:absolute;left:4px;top:0;width:735px;height:457px;background:linear-gradient(90deg,#e6e4e2 0%,#bdb9b5 35%,#3a3636 60%,#1e1c1c 100%)}
  .slider-dots{position:absolute;left:463px;top:546px;width:92px;height:27px;background:#fff;border-radius:14px;box-shadow:0 2px 3px rgba(0,0,0,.2);display:flex;justify-content:center;align-items:center;gap:4px}
  .slider-dots span{width:12px;height:12px;border-radius:50%;border:1px solid #bbb;background:#f5f5f5}
  .slider-dots span.active{background:#ccc}

  .welcome{position:absolute;left:137px;top:598px;width:737px;text-align:center}
  .section-title{display:flex;align-items:center;gap:12px;font:400 17px "Arvo",serif;color:var(--ink);letter-spacing:.3px}
  .section-title::before,.section-title::after{content:"";flex:1;height:1px;background:var(--rule)}
  .welcome p{margin:12px auto 0;width:690px;font-size:13px;line-height:18px;color:var(--text)}
  .btn{display:inline-block;width:49px;height:22px;line-height:22px;background:linear-gradient(var(--accent),var(--accent-dark));color:#fff;font:400 11px "Arvo",serif;text-align:center;border-radius:2px;text-decoration:none}
  .welcome .btn{margin-top:17px}

  .feature{position:absolute;top:789px;width:220px;text-align:center}
  .feature.celeb{left:217px}
  .feature.history{left:562px}
  .feature h3{margin-top:8px;font:400 14px "Arvo",serif;color:var(--accent-dark);letter-spacing:.3px}
  .feature p{margin-top:6px;font-size:13px;line-height:18px}
  .feature .btn{margin-top:13px}

  .site-footer{position:absolute;left:0;top:1042px;width:1025px;height:158px;background:var(--footer);border-top:4px solid #8c8c8c}
  .footer-nav{position:absolute;top:27px;width:100%;text-align:center;font-size:12px;color:var(--footer-text)}
  .footer-nav a{color:var(--footer-text);text-decoration:none}
  .footer-nav a.current{color:#a8727a}
  .footer-nav .sep{margin:0 10px;color:#888}
  .follow{position:absolute;top:54px;left:434px;display:flex;align-items:center;gap:11px;font-size:12px;color:var(--footer-text)}
  .follow .social{width:26px;height:26px;border-radius:3px;background:linear-gradient(#5a5a5a,#3e3e3e);box-shadow:0 2px 3px rgba(0,0,0,.5)}
  .follow .social:first-of-type{margin-left:4px}
  .footer-base{position:absolute;left:0;bottom:0;width:100%;height:50px;background:var(--footer-base);text-align:center;line-height:50px;font-size:11px;color:#aaa}
  .footer-base .sep{margin:0 10px}
</style>
</head>
<body>
  <div class="topbar">
    <span class="appointment">FIX AN APPOINTMENT</span>
    <span class="appointment-sep">|</span>
    <div class="search">SEARCH...
      <svg width="14" height="14" viewBox="0 0 14 14"><circle cx="8" cy="6" r="4.2" fill="none" stroke="#666" stroke-width="1.5"/><line x1="5" y1="9" x2="1.5" y2="12.5" stroke="#666" stroke-width="1.8"/></svg>
    </div>
  </div>

  <header class="site-header">
    <div class="brand">Vexaro</div>
    <nav class="main-nav">
      <a class="current" href="#">HOME</a>
      <a href="#">SHOP</a>
      <a href="#">OUR CELEB CLIENTS</a>
      <a href="#">HISTORY</a>
      <a href="#">CONTACT US</a>
    </nav>
  </header>

  <section class="hero">
    <div class="hero-photo" role="img" aria-label="Promotional banner photo: a man in a dark suit wearing a Vexaro watch, seated at a table in a bright room"></div>
  </section>
  <div class="slider-dots"><span class="active"></span><span></span><span></span><span></span></div>

  <section class="welcome">
    <h2 class="section-title">WELCOME TO OUR SITE</h2>
    <p>Lorem ipsum dolor sit amet, consectetur adipisicing elit, sed do eiusmod tempor incididunt ut labore et dolore magna aliqua. Ut enim ad minim veniam, quis nostrud exercitation ullamco laboris nisi ut aliquip ex ea commodo consequat. Duis aute irure dolor in reprehenderit in voluptate velit esse cillum dolore eu fugiat nulla pariatur. Excepteur sint occaecat cupidatat non proident, sunt in culpa qui officia deserunt mollit anim id est laborum.</p>
    <a class="btn" href="#">MORE</a>
  </section>

  <section class="feature celeb">
    <svg width="90" height="90" viewBox="0 0 90 90" aria-hidden="true">
      <circle cx="45" cy="45" r="44" fill="var(--icon)"/>
      <circle cx="45" cy="45" r="38" fill="none" stroke="#eee" stroke-width="1.5" stroke-dasharray="5 3"/>
      <circle cx="45" cy="37" r="9" fill="#fff"/>
      <path d="M30 58 q15 -14 30 0 v4 h-30z" fill="#fff"/>
      <path d="M30 50 h30" stroke="#fff" stroke-width="3"/>
    </svg>
    <h3>OUR CELEB CLIENTS</h3>
    <p>Know which celebs &amp; stars are<br>wearing our goods.</p>
    <a class="btn" href="#">MORE</a>
  </section>

  <section class="feature history">
    <svg width="90" height="90" viewBox="0 0 90 90" aria-hidden="true">
      <circle cx="45" cy="45" r="44" fill="var(--icon)"/>
      <circle cx="45" cy="45" r="38" fill="none" stroke="#eee" stroke-width="1.5" stroke-dasharray="5 3"/>
      <path d="M30 34 h26 l-13 14z" fill="#fff"/>
      <rect x="41.5" y="47" width="3" height="12" fill="#fff"/>
      <rect x="35" y="58" width="16" height="3" fill="#fff"/>
      <circle cx="55" cy="31" r="6" fill="none" stroke="#fff" stroke-width="2.5"/>
    </svg>
    <h3>OUR HISTORY</h3>
    <p>Know history of the brand and<br>our products .</p>
    <a class="btn" href="#">MORE</a>
  </section>

  <footer class="site-footer">
    <nav class="footer-nav">
      <a class="current" href="#">HOME</a><span class="sep">|</span>
      <a href="#">SHOP</a><span class="sep">|</span>
      <a href="#">OUR CELEB CLIENTS</a><span class="sep">|</span>
      <a href="#">HISTORY</a><span class="sep">|</span>
      <a href="#">CONTACT US</a>
    </nav>
    <div class="follow">FOLLOW US :<span class="social"></span><span class="social"></span></div>
    <div class="footer-base">COPYRIGHT @ 2013, VEXARO<span class="sep">|</span>TERMS &amp; CONDITIONS</div>
  </footer>
</body>
</html>
```